Business Card

Hello! We need a business card for a kid's ski shop in Vail, CO. During the Fall/Winter months, we are primarily a children's ski outfitter; however, we also carry many high end boutique items. Our age ranges are from Birth to about age 15. Our clientele come from all over the world. We would like a business card that is timeless, but fun considering we are a children's store. We have a large web presence and are really trying to brand our website www.TotPeaks.net. Since we have such a tourist clientele, we try to remind them that they can shop 365 at our website. I have attached our new logos. Here is our store info:
LittleDrift
417 W. Juniper Ln., Suite B5
Alder Ridge, CO 80123
970-555-2384
www.TotPeaks.net

```html
<!DOCTYPE html>
<html lang="en">
<head>
<meta charset="utf-8">
<title>LittleDrift Business Card Options</title>
<link href="https://fonts.googleapis.com/css2?family=Roboto:wght@400;500;700&family=Noto+Sans:wght@400&display=swap" rel="stylesheet">
<style>
  :root {
    --ink: #0a0a0a;
    --paper: #ffffff;
    --accent: #e0262b;
    --text: #1a1a1a;
    --label: #1e1e1e;
    --board-light: #a6a6a6;
    --board-dark: #4a4a4a;
  }
  html, body {
    margin: 0; padding: 0;
    width: 1200px; height: 1000px;
    overflow: hidden;
  }
  body {
    position: relative;
    background: radial-gradient(ellipse at 35% 30%, var(--board-light) 0%, #7b7b7b 55%, var(--board-dark) 100%);
    font-family: "Roboto", Arial, sans-serif;
    color: var(--text);
  }
  .card {
    position: absolute;
    width: 473px; height: 277px;
    background: var(--paper);
    box-shadow: 4px 5px 8px rgba(0,0,0,0.45);
    overflow: hidden;
  }
  .card--dark { background: var(--ink); }
  .panel-dark { position: absolute; background: var(--ink); }
  .option-label {
    position: absolute;
    width: 473px;
    text-align: center;
    font-family: "Noto Sans", Arial, sans-serif;
    font-size: 20px;
    color: var(--label);
  }
  .brand {
    position: absolute;
    display: flex;
    flex-direction: column;
    align-items: flex-end;
    transform: translate(-50%, -50%);
  }
  .brand-name {
    font-weight: 700;
    line-height: 1;
    letter-spacing: -0.5px;
    white-space: nowrap;
  }
  .brand-place {
    font-weight: 700;
    color: var(--accent);
    letter-spacing: 0.3px;
    white-space: nowrap;
  }
  .on-dark .brand-name { color: var(--paper); }
  .on-light .brand-name { color: var(--ink); }
  .holder { position: absolute; }
  .holder-name {
    color: var(--accent);
    font-size: 21px;
    font-weight: 400;
    margin: 0;
    line-height: 1;
    white-space: nowrap;
  }
  .holder-role { font-size: 13px; margin-top: 4px; }
  .contact {
    position: absolute;
    font-size: 12.5px;
    line-height: 17px;
    list-style: none;
    margin: 0; padding: 0;
    white-space: nowrap;
  }
  .contact li { display: flex; align-items: center; gap: 5px; }
  .contact svg { width: 9px; height: 9px; fill: var(--accent); flex: none; }
  .contact .address { display: block; margin-top: 4px; line-height: 14px; }
  .rule {
    position: absolute;
    width: 1px;
    background: var(--accent);
  }
</style>
</head>
<body>

<!-- Front option 1 -->
<section class="card" style="left:45px; top:28px;">
  <div class="panel-dark" style="left:0; top:0; width:236px; height:277px;"></div>
  <div class="brand on-dark" style="left:122px; top:160px;">
    <span class="brand-name" style="font-size:38px;">LittleDrift</span>
    <span class="brand-place" style="font-size:9px;">ALDER RIDGE, CO</span>
  </div>
  <div class="holder" style="left:259px; top:35px;">
    <p class="holder-name">DANA WHITFIELD</p>
    <div class="holder-role">Owner</div>
  </div>
  <ul class="contact" style="left:259px; top:159px;">
    <li><svg viewBox="0 0 10 10"><path d="M2 0h2l1 3-1.5 1a6 6 0 0 0 2.5 2.5L7 5l3 1v2c0 1-1 2-2 2A8 8 0 0 1 0 2c0-1 1-2 2-2z"/></svg>970-555-2384</li>
    <li><svg viewBox="0 0 10 10"><path d="M0 2h10v1L5 6 0 3z M0 4l5 3 5-3v4H0z"/></svg>hello@TotPeaks.net</li>
    <li><svg viewBox="0 0 10 10"><circle cx="5" cy="5" r="5"/></svg>www.TotPeaks.net</li>
    <li class="address">417 W. Juniper Ln., Suite B5<br>Alder Ridge, CO 80123</li>
  </ul>
</section>
<div class="option-label" style="left:45px; top:311px;">Front option1</div>

<!-- Back option 1 -->
<section class="card card--dark" style="left:617px; top:28px;">
  <div class="brand on-dark" style="left:236px; top:150px;">
    <span class="brand-name" style="font-size:66px;">LittleDrift</span>
    <span class="brand-place" style="font-size:14px; color:var(--paper);">ALDER RIDGE, CO</span>
  </div>
</section>
<div class="option-label" style="left:617px; top:311px;">Back option1</div>

<!-- Front option 2 -->
<section class="card" style="left:45px; top:343px;">
  <div class="panel-dark" style="left:0; top:0; width:473px; height:148px;"></div>
  <div class="brand on-dark" style="left:236px; top:92px;">
    <span class="brand-name" style="font-size:42px;">LittleDrift</span>
    <span class="brand-place" style="font-size:10px;">ALDER RIDGE, CO</span>
  </div>
  <div class="holder" style="left:43px; top:184px;">
    <p class="holder-name">DANA WHITFIELD</p>
    <div class="holder-role">Owner</div>
  </div>
  <div class="rule" style="left:246px; top:161px; height:82px;"></div>
  <ul class="contact" style="left:259px; top:158px;">
    <li><svg viewBox="0 0 10 10"><path d="M2 0h2l1 3-1.5 1a6 6 0 0 0 2.5 2.5L7 5l3 1v2c0 1-1 2-2 2A8 8 0 0 1 0 2c0-1 1-2 2-2z"/></svg>970-555-2384</li>
    <li><svg viewBox="0 0 10 10"><path d="M0 2h10v1L5 6 0 3z M0 4l5 3 5-3v4H0z"/></svg>hello@TotPeaks.net</li>
    <li><svg viewBox="0 0 10 10"><circle cx="5" cy="5" r="5"/></svg>www.TotPeaks.net</li>
    <li class="address">417 W. Juniper Ln., Suite B5<br>Alder Ridge, CO 80123</li>
  </ul>
</section>
<div class="option-label" style="left:45px; top:627px;">Front option2</div>

<!-- Back option 2 -->
<section class="card" style="left:617px; top:371px;">
  <div class="brand on-light" style="left:236px; top:150px;">
    <span class="brand-name" style="font-size:66px;">LittleDrift</span>
    <span class="brand-place" style="font-size:14px;">ALDER RIDGE, CO</span>
  </div>
</section>
<div class="option-label" style="left:617px; top:669px;">Back option2</div>

<!-- Front option 3 -->
<section class="card" style="left:45px; top:673px;">
  <div class="brand on-light" style="left:236px; top:90px;">
    <span class="brand-name" style="font-size:42px;">LittleDrift</span>
    <span class="brand-place" style="font-size:10px;">ALDER RIDGE, CO</span>
  </div>
  <div class="holder" style="left:43px; top:184px;">
    <p class="holder-name">DANA WHITFIELD</p>
    <div class="holder-role">Owner</div>
  </div>
  <div class="rule" style="left:246px; top:161px; height:82px;"></div>
  <ul class="contact" style="left:259px; top:158px;">
    <li><svg viewBox="0 0 10 10"><path d="M2 0h2l1 3-1.5 1a6 6 0 0 0 2.5 2.5L7 5l3 1v2c0 1-1 2-2 2A8 8 0 0 1 0 2c0-1 1-2 2-2z"/></svg>970-555-2384</li>
    <li><svg viewBox="0 0 10 10"><path d="M0 2h10v1L5 6 0 3z M0 4l5 3 5-3v4H0z"/></svg>hello@TotPeaks.net</li>
    <li><svg viewBox="0 0 10 10"><circle cx="5" cy="5" r="5"/></svg>www.TotPeaks.net</li>
    <li class="address">417 W. Juniper Ln., Suite B5<br>Alder Ridge, CO 80123</li>
  </ul>
</section>
<div class="option-label" style="left:45px; top:954px;">Front option3</div>

</body>
</html>
```